we need a business card design for a professional painting business. This company has been up and going for about ten years. However it needs an new logo. we want this business card to be modern eye catching and easy to read. I currently have been looking for VP logos but can not find one that suits our needs. This Design should be Our start to a new beginning.
Industry/Entity Type
Painting
Contact Information for Business Card
Varesko Painting Inc.
Licensed & Insured
Tomas Varesko
Phone(631)384-4562
Fax (555) 846-3021
E-mail vareskopaintinginc@mailorbit.test
Requirements
Must have
- a new logo with  VP and i would like it to be in black and white.
i would also like the front to be a solid black with the logo only and then the back to have the information.

```html
<!DOCTYPE html>
<html lang="en">
<head>
<meta charset="utf-8">
<title>Varesko Painting Inc. – Business Card</title>
<link rel="stylesheet" href="https://fonts.googleapis.com/css2?family=Open+Sans:wght@300;400;700&display=swap">
<style>
  :root {
    --page-bg: #e9e6e1;
    --card-black: #050505;
    --ink-white: #ffffff;
    --ink-soft: #e6e6e6;
    --edge-grey: #bdbdbd;
  }
  * { box-sizing: border-box; margin: 0; padding: 0; }
  html, body {
    width: 1200px; height: 1000px; overflow: hidden;
    background: var(--page-bg);
    font-family: "Open Sans", Arial, sans-serif;
  }
  .stage {
    position: relative; width: 1200px; height: 1000px;
  }
  .card {
    position: absolute;
    width: 700px; height: 400px;
    background: var(--card-black);
    color: var(--ink-white);
    overflow: hidden;
    box-shadow: 0 10px 28px rgba(0,0,0,.28);
  }
  .card--front { left: 250px; top: 60px; }
  .card--back  { left: 250px; top: 540px; }

  .edge-band {
    position: absolute; top: 0; bottom: 0; width: 36px;
  }
  .card--front .edge-band { right: 0; }
  .card--back .edge-band  { left: 0; }

  /* Front */
  .brand {
    position: absolute; left: 70px; top: 110px;
    display: flex; align-items: center; gap: 34px;
  }
  .brand-dot {
    width: 150px; height: 150px; border-radius: 50%;
    background: var(--ink-white); flex: none;
  }
  .brand-name {
    font-weight: 700; font-size: 40px; letter-spacing: 1px;
    text-transform: uppercase; line-height: 1.1;
    color: var(--ink-white);
  }
  .brand-tagline {
    margin-top: 14px;
    font-weight: 300; font-size: 27px; color: var(--ink-soft);
  }

  /* Back */
  .contact {
    position: absolute; left: 90px; top: 120px;
    font-size: 20px; line-height: 1.65; color: var(--ink-soft);
  }
  .contact-name {
    font-weight: 400; font-size: 27px; letter-spacing: 1px;
    text-transform: uppercase; color: var(--ink-white);
    margin-bottom: 6px;
  }
  .contact-label { font-weight: 700; color: var(--ink-white); }
  .back-dot {
    position: absolute; right: 70px; top: 110px;
    width: 150px; height: 150px; border-radius: 50%;
    background: var(--ink-white);
  }
</style>
</head>
<body>
<main class="stage">

  <section class="card card--front" aria-label="Business card front">
    <div class="brand">
      <div class="brand-dot"></div>
      <div class="brand-text">
        <p class="brand-name">Varesko Painting Inc.</p>
        <p class="brand-tagline">Licensed &amp; Insured</p>
      </div>
    </div>
    <svg class="edge-band" viewBox="0 0 36 400" preserveAspectRatio="none" aria-hidden="true">
      <rect x="0" y="0" width="36" height="400" fill="var(--ink-white)"/>
      <rect x="8" y="0" width="2" height="400" fill="var(--edge-grey)"/>
      <rect x="20" y="0" width="1.5" height="400" fill="var(--edge-grey)"/>
    </svg>
  </section>

  <section class="card card--back" aria-label="Business card back">
    <svg class="edge-band" viewBox="0 0 36 400" preserveAspectRatio="none" aria-hidden="true">
      <rect x="0" y="0" width="36" height="400" fill="var(--ink-white)"/>
      <rect x="15" y="0" width="1.5" height="400" fill="var(--edge-grey)"/>
      <rect x="26" y="0" width="2" height="400" fill="var(--edge-grey)"/>
    </svg>
    <div class="contact">
      <p class="contact-name">Tomas Varesko</p>
      <p><span class="contact-label">Telephone:</span> (555)217-9083</p>
      <p><span class="contact-label">Fax:</span> (555) 846-3021</p>
      <p><span class="contact-label">Email:</span> vareskopaintinginc@mailorbit.test</p>
    </div>
    <div class="back-dot"></div>
  </section>

</main>
</body>
</html>
```